Merge product image and small book on 1 photo

Hello

I have an order to place. It involves adding a small book to two measuring devices. Specifically, we need 1 picture each, on which the measuring device and the small book are shown together.

I have illustrated the various combinations in the "Yur job" file. It is your job to create the mockups professionally. You can find the contents of the mockups in the PDF. The page numbers of the pages you can use are noted in the "Your-Job" file.

There are 2 pictures showing the original book: It is A6 sized (15 cm high) and is not very thick (0.5 cm). The two measuring devices are larger. It simply has to look good so that we can present the pictures on the website.

You are welcome to use your own booklet compositions (with AI) or other techniques and do not necessarily have to use the templates. For example, where the book is illustrated with rotating pages - I can certainly use more templates there.

Many thanks in advance.

Best, Gerold

```html
<!DOCTYPE html>
<html lang="de">
<head>
<meta charset="utf-8">
<title>Ratgeber Elektrosmog – Broschüre</title>
<link href="https://fonts.googleapis.com/css2?family=Fira+Sans+Extra+Condensed:wght@500;600;700&family=Open+Sans:ital,wght@0,400;0,600;0,700;1,600&family=Roboto+Slab:wght@600&display=swap" rel="stylesheet">
<style>
:root{
  --red:#d9372a;
  --ink:#1f1f1f;
  --text:#4a4a4a;
  --paper:#ffffff;
  --page:#f7f6f4;
  --grey:#e9e8e6;
  --bg:#ffffff;
}
*{box-sizing:border-box;margin:0;padding:0}
html,body{width:1200px;height:590px;overflow:hidden;background:var(--bg)}
body{position:relative;font-family:"Open Sans",sans-serif;color:var(--text)}

/* Cover */
.cover{position:absolute;left:30px;top:70px;width:320px;height:450px;background:var(--paper);overflow:hidden;box-shadow:0 4px 14px rgba(0,0,0,.18)}
.brand{position:absolute;left:20px;top:40px;display:flex;align-items:center;gap:6px}
.brand-dot{width:12px;height:12px;background:var(--red);border-radius:50%}
.brand-name{font-family:"Open Sans",sans-serif;font-weight:700;font-size:22px;color:var(--ink);letter-spacing:1px}
.cover-chevrons{position:absolute;left:132px;top:62px}
.cover-note{position:absolute;left:168px;top:22px;font-family:"Roboto Slab",serif;font-weight:600;font-size:16px;line-height:20px;color:var(--ink)}
.photo-device{position:absolute;left:118px;top:78px;width:240px;height:240px;border-radius:50%;background:radial-gradient(circle at 55% 45%,#f4f4f4,#cfd2d4 70%)}
.photo-family{position:absolute;left:26px;top:170px;width:128px;height:128px;border-radius:50%;background:linear-gradient(160deg,#8a9ca8,#6f8a4e 55%,#d38a3a);border:3px solid #fff}
.cover-red{position:absolute;left:0;top:0;width:320px;height:450px}
.cover-title{position:absolute;left:26px;top:308px;font-family:"Fira Sans Extra Condensed",sans-serif;font-weight:700;font-size:33px;line-height:30px;color:var(--ink)}
.cover-pages{position:absolute;right:20px;top:306px;font-family:"Fira Sans Extra Condensed",sans-serif;font-weight:600;font-size:20px;color:#fff}
.cover-sub{position:absolute;left:26px;top:374px;font-family:"Fira Sans Extra Condensed",sans-serif;font-weight:600;font-size:27px;color:#fff}
.cover-tip{position:absolute;left:26px;top:410px;font-style:italic;font-weight:600;font-size:13px;color:#fff}

/* Spread */
.spread{position:absolute;left:380px;top:70px;width:600px;height:430px;display:flex;box-shadow:0 4px 14px rgba(0,0,0,.15)}
.page{position:relative;width:300px;height:430px;background:var(--page);overflow:hidden}
.page-left{border-right:1px solid #ddd}
.band{position:absolute;left:0;top:0}
.page-num-top{position:absolute;left:20px;top:16px;font-family:"Fira Sans Extra Condensed",sans-serif;font-weight:700;font-size:18px;color:#fff}
.h-small{font-family:"Fira Sans Extra Condensed",sans-serif;font-weight:600;font-size:12.5px;color:var(--ink)}
.body{font-size:8.6px;line-height:12.6px;color:var(--text)}
.left-head{position:absolute;left:20px;top:70px}
.left-p1{position:absolute;left:22px;top:86px;width:262px}
.left-p2{position:absolute;left:22px;top:226px;width:170px}
.left-p2 b{color:var(--ink);font-weight:600}
.hand-photo{position:absolute;left:200px;top:180px;width:100px;height:140px;border-radius:40px 0 0 40px;background:linear-gradient(180deg,#f08a3c,#f2c4a6)}
.grey-wave{position:absolute;left:0;bottom:0}
.quick-head{position:absolute;left:20px;top:322px;font-size:14px}
.ticks{position:absolute;left:20px;top:344px;list-style:none}
.ticks li{display:flex;align-items:center;gap:6px;height:24px;font-family:"Fira Sans Extra Condensed",sans-serif;font-weight:500;font-size:11px;color:var(--ink)}
.footer{position:absolute;bottom:14px;display:flex;align-items:center;gap:6px;font-family:"Fira Sans Extra Condensed",sans-serif;font-weight:600;font-size:10.5px;color:var(--ink)}
.footer .url{color:var(--red)}
.footer .num{background:var(--red);color:#fff;padding:2px 10px}
.footer-left{right:0}
.footer-right{left:0}

.kicker{position:absolute;left:20px;top:58px;font-family:"Fira Sans Extra Condensed",sans-serif;font-weight:600;font-size:15px;color:var(--red)}
.right-title{position:absolute;left:20px;top:78px;font-family:"Fira Sans Extra Condensed",sans-serif;font-weight:700;font-size:24px;line-height:27px;color:var(--ink)}
.right-p{position:absolute;left:20px;top:142px;width:260px}
.feature{position:absolute;left:20px;width:262px;display:flex;gap:10px}
.feature-icon{flex:none;width:38px;height:38px;border-radius:50%;background:var(--red);display:flex;align-items:center;justify-content:center}
.feature h3{font-family:"Fira Sans Extra Condensed",sans-serif;font-weight:600;font-size:10px;color:var(--red)}
.f1{top:246px}
.f2{top:306px}

/* Measuring device */
.device-photo{position:absolute;left:1010px;top:155px;width:86px;height:350px;border-radius:12px;background:linear-gradient(180deg,#c9ccd0 0%,#d8dadd 45%,#f26a21 46%,#e85c14 100%)}
</style>
</head>
<body>

<section class="cover" aria-label="Titelseite">
  <div class="photo-device" role="img" aria-label="Foto zweier Elektrosmog-Messgeräte"></div>
  <div class="photo-family" role="img" aria-label="Foto einer Familie vor ihrem Haus"></div>
  <svg class="cover-red" viewBox="0 0 320 450" aria-hidden="true">
    <path d="M0 268 Q170 300 320 240 L320 450 L0 450 Z" fill="var(--red)"/>
  </svg>
  <div class="brand"><span class="brand-dot"></span><span class="brand-name">NOVIS</span></div>
  <svg class="cover-chevrons" width="30" height="30" viewBox="0 0 30 30" aria-hidden="true">
    <path d="M2 12 L14 22 L26 4" fill="none" stroke="var(--red)" stroke-width="5"/>
    <path d="M6 22 L14 28 L24 16" fill="none" stroke="var(--red)" stroke-width="4"/>
  </svg>
  <div class="cover-note">Inkl. Anleitung zu<br>den Messgeräten</div>
  <div class="cover-title">RATGEBER<br>ELEKTROSMOG</div>
  <div class="cover-pages">72 Seiten</div>
  <div class="cover-sub">Strahlung aufspüren</div>
  <div class="cover-tip">» Tipps für zu Hause und im Büro</div>
</section>

<section class="spread" aria-label="Aufgeschlagene Doppelseite">
  <article class="page page-left">
    <svg class="band" width="300" height="60" viewBox="0 0 300 60" aria-hidden="true">
      <path d="M0 0 H300 V48 Q150 52 0 8 Z" fill="var(--red)"/>
    </svg>
    <h2 class="h-small left-head">24 LED-ANZEIGEN GRÜN BIS ROT</h2>
    <p class="body left-p1">Das Messgerät detektiert Hochfrequenz (HF), Niederfrequenz (NF) sowie Elektrische Felder gleichzeitig, wenn Sie messen. Dazu gehören Computer, Sicherungs-Schaltkästen, Lampen, Netzteile, Hochspannungsleitungen, Transformatoren, Wechselrichter, Mobilfunkmasten, WiFi/WLAN, Schnurlostelefone. Die Anzeige erfolgt über die 3 LED-Bahnen (von links nach rechts von grün bis rot). Grün bedeutet: keine messbare Strahlung. Je mehr sich die Anzeige rot nähert, desto stärker ist die Belastung.</p>
    <p class="body left-p2"><b>Rot bedeutet:</b> Überschreitung der im Gerät hinterlegten baubiologischen Grenzwerte (nicht der offiziellen von Behörden festgesetzten Grenzwerte). Diese sind höher. Bei rot ist eine genaue Profi-Messung durch uns zu empfehlen.</p>
    <svg class="grey-wave" width="300" height="120" viewBox="0 0 300 120" aria-hidden="true">
      <path d="M0 20 Q150 -10 300 40 V120 H0 Z" fill="var(--grey)"/>
    </svg>
    <div class="hand-photo" role="img" aria-label="Foto einer Hand, die das Messgerät hält"></div>
    <h2 class="h-small quick-head">RASCH UND UNKOMPLIZIERT</h2>
    <ul class="ticks">
      <li><svg width="16" height="14" viewBox="0 0 16 14" aria-hidden="true"><path d="M1 7 L6 12 L15 1" fill="none" stroke="var(--red)" stroke-width="3"/></svg>Unkomplizierte Erkennung von 4G / 5G usw.</li>
      <li><svg width="16" height="14" viewBox="0 0 16 14" aria-hidden="true"><path d="M1 7 L6 12 L15 1" fill="none" stroke="var(--red)" stroke-width="3"/></svg>Einfach bedienbar - für Private und Unternehmen</li>
    </ul>
    <div class="footer footer-left">RATGEBER <span class="url">www.novis-ratgeber.example</span><span class="num">63</span></div>
  </article>

  <article class="page page-right">
    <svg class="band" width="300" height="50" viewBox="0 0 300 50" aria-hidden="true">
      <path d="M0 0 H300 V8 Q200 46 0 42 Z" fill="var(--red)"/>
    </svg>
    <div class="page-num-top">8</div>
    <div class="kicker">NACHT &amp; SCHLAF</div>
    <h1 class="right-title">STRAHLT IHRE<br>NACHTTISCHLAMPE?</h1>
    <p class="body right-p">Was viele nicht wissen: Ihre Nachttischlampe strahlt die ganze Nacht. Falsch in der Steckdose eingesteckt, steht die ganze Nachttischlampe unter Spannung - auch wenn sie ausgeschaltet ist und das Licht nicht brennt. Sie verbreitet meterweit ein elektrisches Feld. Die ganze Nacht. Oft schläft man mit dem Kopf direkt daneben.</p>
    <div class="feature f1">
      <div class="feature-icon"><svg width="20" height="20" viewBox="0 0 20 20" aria-hidden="true"><circle cx="10" cy="10" r="8.5" fill="none" stroke="#fff" stroke-width="1.6"/><path d="M11 3 L6 11 H10 L9 17 L14 9 H10 Z" fill="#fff"/></svg></div>
      <div><h3>ELEKTRISCHES FELD DIE GANZE NACHT</h3><p class="body">Jede Nachttischlampe verbreitet ein elektrisches Feld. Die Lampe strahlt genauso stark auch in ausgeschaltetem Zustand, die ganze Nacht!</p></div>
    </div>
    <div class="feature f2">
      <div class="feature-icon"><svg width="22" height="16" viewBox="0 0 22 16" aria-hidden="true"><path d="M4 2 H18 L21 8 L18 14 H4 L1 8 Z" fill="none" stroke="#fff" stroke-width="1.8"/><circle cx="7" cy="7" r="1.6" fill="#fff"/><circle cx="15" cy="7" r="1.6" fill="#fff"/><circle cx="11" cy="11" r="1.6" fill="#fff"/></svg></div>
      <div><h3>DER TRICK MIT DEM STECKER</h3><p class="body">Mit einem einfachen Trick lässt sich die Strahlung komplett eliminieren. Ziehen Sie den Stecker aus, drehen Sie ihn um und stecken Sie ihn wieder ein. Jetzt ist die Strahlung weg. Der Grund des Phänomens: Phase und Leiter des Steckers sind verdreht. Das sieht man dem Stecker leider nicht an.</p></div>
    </div>
    <div class="footer footer-right"><span class="num">32</span>RATGEBER <span class="url">www.novis-ratgeber.example</span></div>
  </article>
</section>

<div class="device-photo" role="img" aria-label="Foto des orangen Handmessgeräts mit drei LED-Reihen"></div>

</body>
</html>
```